依頼詳細
以下がデザインについて重視するポイントです。

1.書籍タイトルが目立つように
Gridshelfで書籍アプリとして販売するため、書籍タイトル「明日から変わる 前進の行動論」がハッキリと読み取れるようなデザインを依頼致します。
velkorでは57ピクセルで表示されるため、小さいサイズでも文字が読み取れるように意識してください。

2.知的でシンプルに洗練されたイメージを訴求したい
このアプリは、学術的な研究・論文を下敷きにしながら「成功の法則」を解説する本です。
したがって、デザインは読者に、知的で洗練された印象を与えられるようなものを希望致します。フォントや配色に反映させて頂ければ幸いです。

3.文字にプラスαを
文字だけのデザインだと単調になるため、テーマにあうアイコンやシルエットなどのワンポイントをデザインにくわえてください。参考までに、過去のコンペで採用したデザインはこち
http://www.kobaten.jp/profile/moriha/feedback/

4.コンペに提出するサイズは57×57のサイズを含めてください。
実際にVelkorで見る際には、57×57ピクセルで表示されます。実際のイメージがわくように、57×57のサイズのデータをコンペに提出してください。
記載項目
1.デザインに反映させる内容
アプリのメインに「前進の行動論」を使用。サブタイトルとして「明日から変わる」をアプリのデザインに反映してください。メインとサブは主従の関係になるように。

2,サイズは以下のサイズをお願い致します。
1024 x 1024 px(melodex用)
144×144 px(Tablix Klarview用)
114 x 114 px(Velkor Klarview用)
72 × 72px(Tablix用)
57 x 57 px(Velko用)
希望イメージ
シンプル 複雑
単色 カラフル
暗い 明るい
日常 高級
遊び心 厳粛
未来的 伝統的
女性的 男性的
希望する色
青、緑、黒などの落ち着いた印象、知的な印象を与えるベース色を希望致します。
納品ファイル
• イラストレーター形式 (.ai)
• PNG形式 (.png)
補足説明
提案数が少なかったため、金額を増やし、募集期間を延長しました。
■ 選んだ理由

アイコンにおける文字の見栄えがよく、Gridshelf上で目立つと感じたためです。特に、修正案で提出頂いたセンターの案が優れていると感じました。

■ 提案者全員のお礼・コメント

どの方の提案も要望をとりいれたものが多く、選定が大変でした。また、コバテンで依頼することになるとおもいます。その際はまたよろしくお願いいたします。

```html
<!DOCTYPE html>
<html lang="ja">
<head>
<meta charset="utf-8">
<title>明日から変わる 前進の行動論 — アプリアイコン</title>
<link rel="stylesheet" href="https://fonts.googleapis.com/css2?family=Noto+Sans+JP:wght@700;900&display=swap">
<style>
  :root {
    --page-bg: #ffffff;
    --sky-deep: #1f63c8;
    --sky-mid: #4f95e3;
    --sky-light: #cfe3f7;
    --sun-white: #ffffff;
    --ribbon-white: #ffffff;
    --ribbon-edge: #2a2a2a;
    --ribbon-shade: #c9ced6;
    --accent-red: #c8202a;
    --kana-dark: #3a3a3a;
    --title-yellow-top: #fff35a;
    --title-yellow-bottom: #f5a400;
    --title-outline: #2b1a06;
    --title-glow: #e9f6ff;
  }
  html, body {
    margin: 0;
    padding: 0;
    width: 1200px;
    height: 1200px;
    overflow: hidden;
    background: var(--page-bg);
  }
  .app-icon {
    display: block;
    width: 1200px;
    height: 1200px;
  }
  .subtitle-text {
    font-family: "Noto Sans JP", sans-serif;
    font-weight: 900;
  }
  .title-text {
    font-family: "Noto Sans JP", sans-serif;
    font-weight: 900;
  }
</style>
</head>
<body>
<svg class="app-icon" viewBox="0 0 1200 1200" xmlns="http://www.w3.org/2000/svg">
  <defs>
    <clipPath id="icon-shape">
      <rect x="120" y="120" width="954" height="954" rx="48"/>
    </clipPath>
    <linearGradient id="sky-fill" x1="0" y1="0" x2="0" y2="1">
      <stop offset="0" stop-color="var(--sky-deep)"/>
      <stop offset="0.45" stop-color="var(--sky-mid)"/>
      <stop offset="1" stop-color="var(--sky-light)"/>
    </linearGradient>
    <radialGradient id="sun-glow" cx="0.5" cy="0.38" r="0.45">
      <stop offset="0" stop-color="var(--sun-white)" stop-opacity="1"/>
      <stop offset="0.35" stop-color="var(--sun-white)" stop-opacity="0.6"/>
      <stop offset="1" stop-color="var(--sun-white)" stop-opacity="0"/>
    </radialGradient>
    <linearGradient id="title-fill" x1="0" y1="0" x2="0" y2="1">
      <stop offset="0" stop-color="var(--title-yellow-top)"/>
      <stop offset="0.55" stop-color="#ffd21a"/>
      <stop offset="1" stop-color="var(--title-yellow-bottom)"/>
    </linearGradient>
  </defs>

  <g clip-path="url(#icon-shape)">
    <rect class="sky-backdrop" x="120" y="120" width="954" height="954" fill="url(#sky-fill)"
          role="img" aria-label="Photo of skyscrapers seen from below against a blue sky with a bright sunburst"/>
    <rect x="120" y="120" width="954" height="954" fill="url(#sun-glow)"/>
  </g>

  <g class="ribbon-banner">
    <polygon points="120,300 215,300 215,395 170,370 120,395" fill="var(--ribbon-shade)" stroke="var(--ribbon-edge)" stroke-width="4"/>
    <polygon points="1074,300 980,300 980,395 1025,370 1074,395" fill="var(--ribbon-shade)" stroke="var(--ribbon-edge)" stroke-width="4"/>
    <path d="M165 165 Q600 135 1030 165 L1030 360 Q600 330 165 360 Z" fill="var(--ribbon-white)" stroke="var(--ribbon-edge)" stroke-width="5"/>
    <text class="subtitle-text" x="600" y="300" text-anchor="middle" font-size="96">
      <tspan fill="var(--accent-red)">明日</tspan><tspan fill="var(--kana-dark)" font-size="72">から</tspan><tspan fill="var(--accent-red)">変わる</tspan>
    </text>
  </g>

  <g class="main-title">
    <g stroke-linejoin="round">
      <text class="title-text" x="600" y="720" text-anchor="middle" font-size="185" fill="none" stroke="var(--title-glow)" stroke-width="34">前進の</text>
      <text class="title-text" x="600" y="720" text-anchor="middle" font-size="185" fill="url(#title-fill)" stroke="var(--title-outline)" stroke-width="12" paint-order="stroke">前進の</text>
    </g>
    <g stroke-linejoin="round">
      <text class="title-text" x="600" y="945" text-anchor="middle" font-size="240" fill="none" stroke="var(--title-glow)" stroke-width="38">行動論</text>
      <text class="title-text" x="600" y="945" text-anchor="middle" font-size="240" fill="url(#title-fill)" stroke="var(--title-outline)" stroke-width="14" paint-order="stroke">行動論</text>
    </g>
  </g>
</svg>
</body>
</html>
```